Design Health Food E-Book for Small Business Using Provided Content

My business is looking for a designer to design and create an e-book PDF with recipes and images.

The required work will be:

Designing layout of e-book based on provided (below) e-book sample.

Adding supplied recipes and images into a PDF format

Iterating PDF until the work has reached satisfactory requirements

The outcome will be:

1 PDF document (roughly 10-15 pages) created using supplied recipes and images

This recipe e-book by Tessa Morrow should serve as a strong piece of inspiration.

https://brightplatekitchen.example.com/item/7c41d2e9a0f3b615397e8b04

The full content of the e-book, including photos and copy, can be found here:

https://files.example-share.net/sh/kqe915tz47w203x/BBxRnugwXMpoHeTvQjKsZWy4Fb?dl=0

Please arrange for a skype conversation if further clarification of e-book output and/or design are necessary.

Email: rowlet819@mailbrook.net

Industry/Entity Type

Health And Wellness

Font styles to use
Other font styles liked:
• Designer Choice

Requirements
Must have
• Book-like appearance (as in actually looks like a recipe book as opposed to a flyer, photo collection etc.
• Flawless page-linking (from contents page and to external sources) and no errors in text (unless we put a typo in!)
• Cute extra graphics (as per supplied Tessa Morrow book)
Nice to have
• Designer interested in health food
• Experience in e-book design
Should not have
• Typos
• Errors in text linking

```html
<!DOCTYPE html>
<html lang="en">
<head>
<meta charset="utf-8">
<title>Savoury Beetroot Crepes – Recipe Spread</title>
<link href="https://fonts.googleapis.com/css2?family=Arvo:wght@700&family=Special+Elite&family=Open+Sans:wght@300;400;700&display=swap" rel="stylesheet">
<style>
  :root {
    --backdrop: #e4e2dd;
    --leaf: #9cc33b;
    --leaf-dark: #86ad2b;
    --ink: #3a3a3a;
    --card: #ffffff;
    --card-shade: #f1f1f1;
    --white: #ffffff;
  }
  * { box-sizing: border-box; margin: 0; padding: 0; }
  html, body { width: 1200px; height: 804px; overflow: hidden; }
  body {
    background: var(--backdrop);
    font-family: "Open Sans", Arial, sans-serif;
    color: var(--ink);
    position: relative;
  }
  .spread {
    position: absolute; left: 60px; top: 32px;
    width: 1080px; height: 740px;
    display: flex;
    box-shadow: 0 6px 24px rgba(0,0,0,.18);
  }
  .page { position: relative; width: 540px; height: 740px; overflow: hidden; }
  .page__photo { position: absolute; inset: 0; }
  .page--left .page__photo {
    background: radial-gradient(ellipse at 50% 45%, #6d5a3e 0%, #8b7654 25%, #b9b2a6 55%, #d8d4cc 80%);
  }
  .page--right .page__photo {
    background: radial-gradient(ellipse at 60% 40%, #d9d2bf 0%, #8c3a3a 30%, #6a1f26 55%, #5a3b2a 80%, #8c8c90 100%);
  }
  .page__spine-shade { position: absolute; top: 0; bottom: 0; width: 40px; }
  .page--left .page__spine-shade { right: 0; background: linear-gradient(90deg, transparent, rgba(0,0,0,.18)); }
  .page--right .page__spine-shade { left: 0; background: linear-gradient(270deg, transparent, rgba(0,0,0,.18)); }
  .corner-tab { position: absolute; top: 0; width: 60px; height: 22px; background: var(--leaf); }
  .page--left .corner-tab { right: 0; clip-path: polygon(0 0, 100% 0, 100% 100%); }
  .page--right .corner-tab { left: 0; clip-path: polygon(0 0, 100% 0, 0 100%); }
  .page-number {
    position: absolute; bottom: 0; width: 50px; height: 34px;
    background: var(--leaf); color: var(--white);
    font-size: 11px; font-weight: 700;
    display: flex; align-items: flex-end; padding: 0 10px 6px;
  }
  .page--left .page-number { left: 0; clip-path: polygon(0 30%, 100% 100%, 0 100%); }
  .page--right .page-number { right: 0; justify-content: flex-end; clip-path: polygon(100% 30%, 100% 100%, 0 100%); }

  .recipe-title { position: absolute; left: 40px; top: 70px; display: flex; gap: 12px; }
  .recipe-title__thumb {
    width: 86px; height: 78px; border: 3px solid var(--white);
    box-shadow: 0 2px 6px rgba(0,0,0,.3);
  }
  .page--left .recipe-title__thumb { background: linear-gradient(160deg, #d9d4ca, #6d5a3e 55%, #c0453b); }
  .page--right .recipe-title__thumb { background: linear-gradient(160deg, #7a2530, #a84848 50%, #cfc9b2); }
  .recipe-title__text { font-family: "Arvo", Georgia, serif; font-weight: 700; font-size: 27px; line-height: 1.15; padding-top: 4px; }
  .recipe-title__lead { color: var(--leaf); text-shadow: 0 1px 3px rgba(0,0,0,.25); }
  .recipe-title__main { color: var(--white); text-shadow: 0 1px 3px rgba(0,0,0,.35); }
  .recipe-title__day { font-family: "Open Sans", Arial, sans-serif; font-weight: 300; }

  .card {
    position: absolute; background: linear-gradient(180deg, var(--card), var(--card-shade));
    clip-path: polygon(24px 0, 100% 0, 100% 100%, 0 100%, 0 24px);
    padding: 18px 14px 14px;
    box-shadow: 0 2px 10px rgba(0,0,0,.2);
  }
  .card--needs { left: 122px; top: 328px; width: 186px; height: 392px; }
  .card--method { left: 318px; top: 350px; width: 186px; height: 350px; }
  .card__head { display: flex; align-items: center; gap: 10px; }
  .card__meta { font-size: 8.5px; color: var(--leaf-dark); line-height: 1.3; }
  .card__meta b { color: var(--ink); font-weight: 400; }
  .card__title {
    font-family: "Special Elite", "Courier New", monospace;
    color: var(--leaf-dark); font-size: 17px; margin: 12px 0 10px;
  }
  .section-label {
    display: flex; align-items: center; justify-content: space-between;
    font-weight: 700; font-size: 9px; text-transform: uppercase; margin: 8px 0 4px;
  }
  .list { list-style: none; font-size: 8.3px; line-height: 1.35; }
  .list li { position: relative; padding-left: 10px; margin-bottom: 2px; }
  .list li::before { content: "•"; position: absolute; left: 0; }
  .steps { list-style: none; font-size: 8.3px; line-height: 1.35; counter-reset: step; }
  .steps li { position: relative; padding-left: 16px; margin-bottom: 3px; counter-increment: step; }
  .steps li::before { content: counter(step) "."; position: absolute; left: 0; }
  .icon { width: 22px; height: 22px; flex: none; }
</style>
</head>
<body>
<svg width="0" height="0" style="position:absolute">
  <defs>
    <symbol id="cutlery" viewBox="0 0 40 40">
      <line x1="6" y1="34" x2="32" y2="8" stroke="#444" stroke-width="3.5" stroke-linecap="round"/>
      <line x1="8" y1="8" x2="34" y2="34" stroke="#444" stroke-width="3.5" stroke-linecap="round"/>
      <path d="M28 4 L36 12" stroke="#444" stroke-width="2"/>
      <path d="M30 3 L37 10" stroke="#444" stroke-width="1.5"/>
    </symbol>
    <symbol id="timer" viewBox="0 0 24 24">
      <circle cx="8" cy="15" r="6" fill="none" stroke="#444" stroke-width="2"/>
      <path d="M8 12 V15 H10" stroke="#444" stroke-width="1.6" fill="none"/>
      <rect x="14" y="4" width="2" height="9" fill="#444"/>
      <circle cx="18" cy="18" r="4" fill="#444"/>
    </symbol>
    <symbol id="bowl-down" viewBox="0 0 24 24">
      <circle cx="12" cy="12" r="10" fill="none" stroke="#444" stroke-width="2"/>
      <path d="M12 6 V15 M8 11 L12 15 L16 11 M7 17 H17" stroke="#444" stroke-width="2" fill="none"/>
    </symbol>
    <symbol id="mortar" viewBox="0 0 24 24">
      <path d="M2 11 H22 Q21 21 12 21 Q3 21 2 11 Z" fill="#222"/>
      <line x1="14" y1="10" x2="21" y2="2" stroke="#222" stroke-width="3" stroke-linecap="round"/>
    </symbol>
  </defs>
</svg>

<main class="spread">
  <section class="page page--left">
    <div class="page__photo" role="img" aria-label="Stack of blueberry oat pancakes on a plate with strawberries, held in front of a white knit top"></div>
    <div class="page__spine-shade"></div>
    <div class="corner-tab"></div>
    <header class="recipe-title">
      <div class="recipe-title__thumb" role="img" aria-label="Thumbnail of the pancake stack"></div>
      <h1 class="recipe-title__text">
        <span class="recipe-title__lead">Savoury Beetroot</span><br>
        <span class="recipe-title__main">Crepes <span class="recipe-title__day">- FRIDAY</span></span>
      </h1>
    </header>

    <article class="card card--needs">
      <div class="card__head">
        <svg class="icon" style="width:34px;height:34px"><use href="#cutlery"/></svg>
        <p class="card__meta">Servings: <b>x2</b><br>GF, DF, Vegan, RSF</p>
      </div>
      <h2 class="card__title">YOU WILL NEED</h2>
      <div class="section-label">For the crepes: <svg class="icon"><use href="#timer"/></svg></div>
      <ul class="list">
        <li>2 medium beetroots, finely grated</li>
        <li>1 cup buckwheat or brown rice flour</li>
        <li>1 cup unsweetened almond milk or other plant milk</li>
        <li>1 flax egg</li>
        <li>1 Tbsp. coconut or olive oil</li>
        <li>1 tsp salt</li>
      </ul>
      <div class="section-label">Suggested fillings: <svg class="icon"><use href="#bowl-down"/></svg></div>
      <ul class="list">
        <li>Fresh baby spinach or rocket leaves</li>
        <li>Mashed avocado</li>
      </ul>
      <div class="section-label">Homemade hummus: <svg class="icon"><use href="#mortar"/></svg></div>
      <ul class="list">
        <li>Mashed cannellini beans</li>
      </ul>
    </article>

    <article class="card card--method">
      <h2 class="card__title" style="margin-top:4px">HOW TO:</h2>
      <ol class="steps">
        <li>Combine all ingredients in a large bowl and stir to combine well</li>
        <li>Heat half the oil over medium heat in a large crepe pan (or frying pan) and sprinkle over half the salt</li>
        <li>Pour half the beetroot mixture into the pan and spread around to evenly coat the pan (use the back of a spoon if necessary)</li>
        <li>Cook for around 5 minutes until the bottom of the crepe is starting to turn golden brown, then carefully flip and continue to cook for another 2 minutes on the other side</li>
        <li>Remove the crepe from the pan and repeat for the second half of the batter</li>
        <li>Serve the crepes filled with homemade hummus, mashed avocado, greens, cannellini beans or your favourite combination of fillings</li>
      </ol>
    </article>
    <div class="page-number">4</div>
  </section>

  <section class="page page--right">
    <div class="page__photo" role="img" aria-label="Beetroot crepe filled with mashed avocado, white beans and greens on a wooden board"></div>
    <div class="page__spine-shade"></div>
    <div class="corner-tab"></div>
    <header class="recipe-title">
      <div class="recipe-title__thumb" role="img" aria-label="Thumbnail of the filled beetroot crepe"></div>
      <h1 class="recipe-title__text">
        <span class="recipe-title__lead">Savoury Beetroot</span><br>
        <span class="recipe-title__main">Crepes <span class="recipe-title__day">- FRIDAY</span></span>
      </h1>
    </header>

    <article class="card card--needs">
      <div class="card__head">
        <svg class="icon" style="width:34px;height:34px"><use href="#cutlery"/></svg>
        <p class="card__meta">Servings: <b>x2</b><br>GF, DF, Vegan, RSF</p>
      </div>
      <h2 class="card__title">YOU WILL NEED</h2>
      <div class="section-label">For the crepes: <svg class="icon"><use href="#timer"/></svg></div>
      <ul class="list">
        <li>2 medium beetroots, finely grated</li>
        <li>1 cup buckwheat or brown rice flour</li>
        <li>1 cup unsweetened almond milk or other plant milk</li>
        <li>1 flax egg</li>
        <li>1 Tbsp. coconut or olive oil</li>
        <li>1 tsp salt</li>
      </ul>
      <div class="section-label">Suggested fillings: <svg class="icon"><use href="#bowl-down"/></svg></div>
      <ul class="list">
        <li>Fresh baby spinach or rocket leaves</li>
        <li>Mashed avocado</li>
      </ul>
      <div class="section-label">Homemade hummus: <svg class="icon"><use href="#mortar"/></svg></div>
      <ul class="list">
        <li>Mashed cannellini beans</li>
      </ul>
    </article>

    <article class="card card--method">
      <h2 class="card__title" style="margin-top:4px">HOW TO:</h2>
      <ol class="steps">
        <li>Combine all ingredients in a large bowl and stir to combine well</li>
        <li>Heat half the oil over medium heat in a large crepe pan (or frying pan) and sprinkle over half the salt</li>
        <li>Pour half the beetroot mixture into the pan and spread around to evenly coat the pan (use the back of a spoon if necessary)</li>
        <li>Cook for around 5 minutes until the bottom of the crepe is starting to turn golden brown, then carefully flip and continue to cook for another 2 minutes on the other side</li>
        <li>Remove the crepe from the pan and repeat for the second half of the batter</li>
        <li>Serve the crepes filled with homemade hummus, mashed avocado, greens, cannellini beans or your favourite combination of fillings</li>
      </ol>
    </article>
    <div class="page-number">5</div>
  </section>
</main>
</body>
</html>
```